Pitch deck for fundraising for a timber drying business

We have the basic content in a powerpoint but need someone to take that and make an attractive and engaging document for a reader who may see hundreds of these a week so visual impact is key.
We are launching a timber drying business in Australia using an exclusive line of kilns not otherwise available in Australia.
Designs should focus on natural tones and connections with forests and timber, probably with a green (colour) focus.

Target Market(s)

investors, wealthyindividuals

Colors

Designer to choose colors to be used in the design.

Requirements
Nice to have
• Design in Canva or similar

```html
<!DOCTYPE html>
<html lang="en">
<head>
<meta charset="utf-8">
<title>Redgum Ventures – Pitch Deck</title>
<link href="https://fonts.googleapis.com/css2?family=Lato:wght@300;400;700;900&family=Quicksand:wght@500;600&display=swap" rel="stylesheet">
<style>
  :root{
    --lime:#8db53c;
    --lime-soft:#c6c86f;
    --lime-pale:#dfe9b8;
    --olive:#3d4f1f;
    --forest:#5a8a2c;
    --ink:#3a3a3a;
    --grey:#7a7a7a;
    --paper:#ffffff;
    --beige:#ecebd8;
  }
  *{box-sizing:border-box;margin:0;padding:0}
  html,body{width:900px;height:1200px;overflow:hidden;background:var(--paper)}
  body{font-family:"Lato",sans-serif;color:var(--ink)}
  .canvas{position:relative;width:900px;height:1200px;overflow:hidden;background:var(--paper)}
  .stage{position:absolute;left:0;top:0;width:1680px;height:2212px;transform:scale(.5357);transform-origin:0 0}
  .slide{position:absolute;width:500px;height:281px;background:var(--paper);overflow:hidden;box-shadow:0 8px 26px rgba(0,0,0,.28)}
  .abs{position:absolute}
  .heading{position:absolute;font-family:"Lato",sans-serif;font-weight:400;color:var(--lime);font-size:25px;line-height:1.1;letter-spacing:.2px;text-transform:uppercase}
  .body{position:absolute;font-size:5.2px;line-height:1.45;color:var(--grey);text-align:justify}
  .body p{margin-bottom:4px}
  .caption{position:absolute;font-size:6px;line-height:1.35;color:var(--grey);text-align:center}
  .squares{position:absolute;display:flex;gap:3px}
  .squares i{display:block;width:9px;height:9px}
  .squares i:nth-child(1){background:var(--olive)}
  .squares i:nth-child(2){background:var(--forest)}
  .squares i:nth-child(3){background:var(--lime)}
  .page-no{position:absolute;right:23px;bottom:9px;font-size:5px;color:var(--ink)}
  .photo{position:absolute}

  .title-veil{position:absolute;left:-70px;top:-40px;width:375px;height:360px;border-radius:50%;background:rgba(255,255,255,.82)}
  .title-main{position:absolute;left:36px;top:114px;width:240px;text-align:center;font-family:"Quicksand",sans-serif;font-weight:600;font-size:26px;color:#3b3b3b;letter-spacing:.6px}
  .title-sub{position:absolute;left:36px;top:144px;width:240px;text-align:center;font-family:"Quicksand",sans-serif;font-weight:500;font-size:22px;color:#3b3b3b}
  .title-rule{position:absolute;left:36px;width:240px;height:2px;background:var(--lime)}
  .title-tag{position:absolute;left:30px;width:252px;text-align:center;font-size:7px;letter-spacing:1.6px;font-weight:700;color:#333}

  .step{position:absolute;left:42px;width:165px;font-size:6.5px;color:var(--grey);padding-bottom:4px;border-bottom:1px solid #ddd}
  .step b{font-weight:400;margin-right:6px}

  .bullets{position:absolute;list-style:none;font-size:6.4px;line-height:1.35;color:var(--grey)}
  .bullets li{position:relative;padding-left:12px;margin-bottom:6px}
  .bullets li::before{content:"➢";position:absolute;left:0;top:0;font-size:5.5px}

  .post-panel{position:absolute;left:0;top:0;width:185px;height:281px;background:var(--lime-soft)}
  .post-word{position:absolute;left:38px;font-size:24px;font-weight:700;color:#fff;letter-spacing:2.5px}

  .about{background:#000}
  .about .body{color:#f2f2f2}

  .adv{background:linear-gradient(120deg,#fbf6ea 0%,#f6ecd8 45%,#fbf5e8 70%,#f3e6cf 100%)}
  .ticks{position:absolute;left:40px;top:58px;width:440px;list-style:none;font-size:5.3px;line-height:1.4;color:#333}
  .ticks li{position:relative;padding-left:16px;margin-bottom:6.3px}
  .ticks li svg{position:absolute;left:0;top:0}
  .ticks b{font-weight:700}

  .phase{position:absolute;left:44px;font-size:10px}
  .phase-list{position:absolute;left:44px;width:200px;font-size:4.6px;line-height:1.4;color:var(--grey);list-style:none}
  .phase-list li::before{content:"•  "}

  .plan-tag{position:absolute;font-size:7.5px;padding:2px 4px}
  .plan-text{position:absolute;font-size:4.6px;line-height:1.4;color:var(--grey)}

  .fin-top{position:absolute;left:0;top:0;width:500px;height:155px;background:linear-gradient(90deg,#3e5225 0%,#4c5f30 55%,#56683a 100%)}
  .fin-col{position:absolute;top:62px;width:100px;font-size:5.6px;line-height:1.3;color:#e9efd6}
  .fin-table{position:absolute;left:27px;top:165px;width:223px;border-collapse:collapse;font-size:5px;color:#333}
  .fin-table th{background:var(--lime);color:#fff;font-weight:400;height:13px}
  .fin-table td{height:15px;border-bottom:2px solid #fff;background:#eef1e2;padding-left:3px}
  .fin-table tr:nth-child(even) td{background:#e1e7cc}
  .chart-card{position:absolute;left:271px;top:125px;width:211px;height:129px;background:#fff;border-radius:6px;box-shadow:0 2px 8px rgba(0,0,0,.25)}

  .member{position:absolute;top:60px;width:80px;text-align:center}
  .member h3{font-size:6px;font-weight:700;letter-spacing:1.4px;color:#555}
  .member p{font-size:4.6px;line-height:2;color:var(--grey);margin-top:5px}
  .member .portrait{width:76px;height:106px;margin:16px auto 0;background:linear-gradient(180deg,#d8dde2 0%,#c6cdd3 45%,#9aa6b3 100%)}
</style>
</head>
<body>
<div class="canvas">
<div class="stage">

  <section class="slide" style="left:267px;top:36px">
    <div class="photo" role="img" aria-label="Tall eucalyptus forest seen from below" style="inset:0;background:linear-gradient(110deg,#9aa28a 0%,#6f7f55 40%,#4f6236 60%,#8d9878 80%,#b6bca8 100%)"></div>
    <div class="title-veil"></div>
    <div class="title-main">Redgum Ventures</div>
    <div class="title-sub">Pitch Deck</div>
    <div class="title-rule" style="top:176px"></div>
    <div class="title-tag" style="top:181px">SUMMIT CAPITAL PARTNERS PRESENTATION</div>
    <div class="title-rule" style="top:192px;left:80px;width:152px;height:1px"></div>
    <div class="title-tag" style="top:196px;font-size:7.5px">Ago 2020</div>
  </section>

  <section class="slide" style="left:922px;top:36px">
    <div class="photo" role="img" aria-label="Close-up of timber end grain rings" style="left:41px;top:29px;width:130px;height:218px;background:linear-gradient(135deg,#c9712c 0%,#e39a5a 35%,#b55a1f 65%,#d8894a 100%)"></div>
    <div class="heading" style="left:146px;top:58px;font-size:26px">Introduction</div>
    <div class="body" style="left:190px;top:95px;width:285px">
      <p>Redgum Ventures International (RVI) has secured exclusive access to a superior timber drying technology (Kilnova kilns) that has been in commercial production since 1980. RVI will leverage this technology to build a hardwood drying business, initially focused on the stair tread market in Sydney and Brisbane.</p>
      <p>Hardwood stair tread timber has an approximate gross margin of $XXXX/m3 (XX%).</p>
      <p>RVI will sell directly to stair tread installers enabling us to retain the bulk of the gross margin as net profit.</p>
      <p>Kilnova kilns are relatively inexpensive ($US79-205K), modular in design, and return approximately 300% per annum. As a result, RVI will be able to scale without additional equity or debt funding.</p>
      <p>The Australian hardwood industry is worth around $7bn pa on 700,000m3 of sawn timber but 93% of logs are exported. With 10 kilns RVI would dry less than 1% of all sawn timber but turn over $XXm and nett $XXm with huge growth potential from value adding exported logs.</p>
      <p>This is not a tech play but a cash cow investment to be held long term. We have a simple business model, using established technology to disrupt a technologically stagnant, but growing industry.</p>
    </div>
    <div class="squares" style="left:41px;top:253px"><i></i><i></i><i></i></div>
    <div class="page-no">2</div>
  </section>

  <section class="slide" style="left:267px;top:345px">
    <div class="heading" style="left:41px;top:60px">Business Model</div>
    <div class="body" style="left:42px;top:95px;width:190px;font-size:6.6px;text-align:left;line-height:1.3">We are using established technology to disrupt the existing timber supply chain with a simple 4 step business model..</div>
    <div class="step" style="top:143px"><b>$XXX m3</b>Buy cut timber from sawmills</div>
    <div class="step" style="top:163px"><b>$XXX m3</b>Dry it in our kilns</div>
    <div class="step" style="top:183px"><b>$XXX m3</b>Dress and deliver</div>
    <div class="step" style="top:203px;border-bottom-color:var(--lime)"><b>$XXX m3</b>Sell dried stair treads to installers</div>
    <div class="step" style="top:223px;border:0"><b>$XXX m3</b>Net profit</div>
    <div class="abs" style="left:300px;top:38px;width:24px;height:25px;background:var(--lime)"></div>
    <div class="abs" style="left:302px;top:142px;width:22px;height:43px;background:var(--lime)"></div>
    <div class="abs" style="left:376px;top:225px;width:67px;height:18px;background:var(--lime)"></div>
    <div class="photo" role="img" aria-label="Timber staircase interior" style="left:324px;top:29px;width:176px;height:196px;background:linear-gradient(140deg,#8a4a22 0%,#c97a3e 45%,#a65a2a 75%,#6b3a1c 100%)"></div>
    <div class="photo" role="img" aria-label="Timber panelled room" style="left:263px;top:65px;width:85px;height:68px;background:linear-gradient(140deg,#7a5236,#b07a4e,#8a6040)"></div>
    <div class="photo" role="img" aria-label="Kiln loaded with stacked timber" style="left:219px;top:133px;width:92px;height:82px;background:linear-gradient(140deg,#4d4d4a,#8c7a5c,#5a5650)"></div>
    <div class="photo" role="img" aria-label="Timber dressing machine" style="left:294px;top:179px;width:82px;height:83px;background:linear-gradient(140deg,#5e6367,#9aa0a4,#6c7175)"></div>
    <div class="squares" style="left:41px;top:253px"><i></i><i></i><i></i></div>
    <div class="page-no">3</div>
  </section>

  <section class="slide" style="left:922px;top:345px">
    <div class="photo" role="img" aria-label="Hardwood stair treads" style="left:41px;top:29px;width:130px;height:206px;background:linear-gradient(160deg,#6a4a2c 0%,#b8642b 45%,#d4803e 70%,#8a4a1f 100%)"></div>
    <div class="abs" style="left:108px;top:215px;width:25px;height:20px;background:var(--forest)"></div>
    <div class="photo" role="img" aria-label="Timber stair with steel balustrade" style="left:136px;top:106px;width:97px;height:147px;background:linear-gradient(150deg,#8a7a66 0%,#c48a52 50%,#9a6a3e 100%)"></div>
    <div class="heading" style="left:184px;top:71px">Why Stair Treads</div>
    <ul class="bullets" style="left:261px;top:110px;width:200px">
      <li>XX% margin</li>
      <li>High absolute $ returns – ~$XXXm3 profit</li>
      <li>Standardised product allowing optimisation of production processes</li>
      <li>Large market – over 65 potential clients indicated interest in purchasing in Sydney alone <sup>1</sup></li>
      <li>Installers looking for alternatives – ~30% of Coastwood products out of specification resulting in no installer profit on those jobs</li>
      <li>Significant drying time advantage over competitors: 1 week v 7-8 months</li>
    </ul>
    <div class="squares" style="left:41px;top:253px"><i></i><i></i><i></i></div>
    <div class="page-no">4</div>
  </section>

  <section class="slide" style="left:267px;top:655px">
    <div class="heading" style="left:41px;top:38px">Market Overview</div>
    <div class="body" style="left:41px;top:77px;width:283px;font-size:4.9px;color:#333">
      <p>The total value of the Australian timber market is $23.9bn¹ with hardwood accounting for over $7bn and softwood the balance. The Australian hardwood market has been growing strongly, posting 10% growth in volume of logs harvested and a 13% increase in price in 2017 despite a 5% fall in housing construction.</p>
      <p>The hardwood industry however is massively under developed with 93%¹ of all plantation hardwood logs being exported – with no value adding.</p>
      <p>The total volume of sawn hardwood timber in 2018 was 700,000m3. With just 10 kilns we would dry less than 6,800m3 pa, gross $30.6m in revenue and net $18.5m with significant opportunity to expand.</p>
      <p>In NSW logs are sourced through either the Northern Ranges Forestry Board (Colin knows and has worked with the Chair previously) on either a quota or spot price basis or through the logging of private forests. RVI will commence by sourcing timber from private forests as there are numerous landholders and contract loggers to ensure timber supply and mitigate sourcing risk.</p>
      <p>To quantify the direct addressable market RVI conducted extensive market research, contacting 98 stair installers, joineries and furniture manufacturers in addition to wholesalers. Stair installers pay between $XXX and $XXXXm3 with an average of just over $XX00m3 whereas wholesalers buy at around $XX00m3.</p>
      <p>Include Alan's timber data on stair tread market</p>
    </div>
    <div class="photo" role="img" aria-label="Stacked hardwood logs in a yard" style="left:341px;top:28px;width:133px;height:224px;background:linear-gradient(180deg,#e9eef0 0%,#b77245 25%,#8a4a2a 60%,#6d8a3e 90%)"></div>
    <div class="squares" style="left:41px;top:253px"><i></i><i></i><i></i></div>
    <div class="page-no">5</div>
  </section>

  <section class="slide" style="left:922px;top:655px">
    <div class="abs" style="left:314px;top:0;width:145px;height:281px;background:var(--olive)"></div>
    <div class="heading" style="left:35px;top:18px;font-size:23px">Comparison of<br>drying techniques</div>
    <div class="abs" style="left:150px;top:73px;font-size:6.5px;color:#222">Competitors</div>
    <div class="abs" style="left:352px;top:73px;font-size:6.5px;color:#fff">Redgum Ventures</div>
    <div class="photo" role="img" aria-label="Green timber stacked to air dry" style="left:56px;top:90px;width:109px;height:100px;background:linear-gradient(180deg,#d9dde0 0%,#a8825e 50%,#7a5a3e 100%)"></div>
    <div class="photo" role="img" aria-label="Conventional drying chamber with fans" style="left:194px;top:90px;width:109px;height:100px;background:linear-gradient(180deg,#c9ccce 0%,#b49674 55%,#8e8a86 100%)"></div>
    <div class="photo" role="img" aria-label="Worker loading a vacuum kiln" style="left:332px;top:90px;width:109px;height:100px;background:linear-gradient(180deg,#6a6a55 0%,#c6a24c 45%,#e0cfae 100%)"></div>
    <div class="caption" style="left:56px;top:202px;width:109px">Green cut timber is left to air dry from 40% moisture to 20-25% taking 6-12 months depending on thickness and weather</div>
    <div class="caption" style="left:194px;top:202px;width:109px">Air dried timber is loaded into an insulated room with multiple fans and a heat source. Drying takes 2-6 weeks for 50mm timber.</div>
    <div class="caption" style="left:325px;top:200px;width:123px;color:#fff">Green timber is loaded into the kiln and automated drying programme for timber species selected. Drying takes 6-7 days to dry 50mm timber in a Kilnova Turbo.</div>
    <div class="abs" style="left:34px;top:252px;width:433px;height:10px;background:var(--beige);border:1px solid #b8b69a"></div>
    <div class="abs" style="left:34px;top:253px;width:280px;text-align:center;font-size:6px;color:#222">Total time 7-14 months</div>
    <div class="abs" style="left:314px;top:253px;width:145px;text-align:center;font-size:6px;color:#222">Total time 7 days</div>
    <div class="page-no">6</div>
  </section>

  <section class="slide" style="left:267px;top:964px">
    <div class="post-panel"></div>
    <div class="post-word" style="top:86px">POST</div>
    <div class="post-word" style="top:131px">DRYING</div>
    <div class="post-word" style="top:176px">PROCESS</div>
    <div class="squares" style="left:41px;top:252px"><i></i><i></i><i></i></div>
    <div class="photo" role="img" aria-label="Dried boards feeding into a thicknesser" style="left:253px;top:21px;width:177px;height:107px;background:linear-gradient(150deg,#3d3a36 0%,#7a6a56 40%,#d8c09a 70%,#5a5048 100%)"></div>
    <div class="body" style="left:253px;top:136px;width:177px;font-size:5.6px">
      <p>Dried stair treads are either delivered skip dressed or sized and finished with volumes being around 50:50 of each. We will commence by offering a skip dressed product as it is the simplest to produce.</p>
      <p>Skip dressing involves running the dried timber through a thicknesser or moulder to roughly level two sides of timber and expose the grain. This allows the quality of the timber grade (Select, Standard or Feature) to be assessed.</p>
      <p>Once dressed, the timber is palletised ready for delivery to the client.</p>
    </div>
    <div class="page-no">7</div>
  </section>

  <section class="slide" style="left:922px;top:964px">
    <div class="heading" style="left:36px;top:30px">Kilnova Kilns</div>
    <div class="body" style="left:36px;top:63px;width:432px;font-size:5.6px;text-align:left">
      <p>The main drying advantage Kilnova kilns have over existing kilns is that they dry in a vacuum. When you dry in a vacuum you lower the boiling point of water, in our case to 20-23C.</p>
      <p>A lower boiling point means less energy is required to evaporate that water but most importantly less stress on the timber whilst doing so. This results in less cracking and warping of timber and hence wastage (5% for Kilnova vs 10-20%).</p>
    </div>
    <div class="body" style="left:36px;top:110px;width:190px;font-size:4.5px">
      <p>The most important operational advantage is their ability to take freshly sawn timber and dry it within a week versus our competitors whose total drying time is 7-8 months at best for 50mm timber.</p>
      <p>The drying time is a factor of two things:</p>
      <p>•  Vacuum: which actively draws moisture from the core of the timber; and<br>•  Direct heating: the Kilnova Turbo uses heating plates between each layer of timber circulating warm water to provide even heating to the top and bottom of each piece of timber</p>
      <p>The result is dried timber that has undergone less stress with fewer defects and more even moisture content, vital for structural integrity. Colours are also richer as the outer core of the timber hasn't been bleached by the high temperatures of traditional kilns attempting to evaporate water.</p>
    </div>
    <div class="photo" role="img" aria-label="Kiln showing heating plates between timber layers" style="left:236px;top:109px;width:109px;height:109px;background:linear-gradient(160deg,#5a5a52 0%,#a89062 50%,#6e6a5e 100%)"></div>
    <div class="photo" role="img" aria-label="Kiln loaded with connected heating plates" style="left:360px;top:109px;width:109px;height:109px;background:linear-gradient(160deg,#1f3150 0%,#3c5a8a 45%,#7a6a52 100%)"></div>
    <div class="caption" style="left:236px;top:230px;width:109px;font-size:4.5px">Kilnova Turbo showing heating plates between timber layers</div>
    <div class="caption" style="left:360px;top:230px;width:109px;font-size:4.5px">Kilnova Turbo loaded with connected heating plates</div>
    <div class="squares" style="left:36px;top:252px"><i></i><i></i><i></i></div>
    <div class="page-no">8</div>
  </section>

  <section class="slide about" style="left:267px;top:1273px">
    <div class="heading" style="left:42px;top:29px;color:#fff">About Kilnova</div>
    <div class="body" style="left:45px;top:80px;width:250px;font-size:5.6px">
      <p>Kilnova is a Vermont family owned business that has been developing and selling vacuum kilns since 1980. Acknowledged as the world leaders in vacuum kiln drying, Kilnova have several patents covering their modularised kilns and control systems.</p>
      <p>Kilnova produces over 150 kilns per annum and has a remote service model which has allowed it to sell kilns in USA, Canada, Mexico, Sweden and New Zealand. Kilnova has also recently opened an office in Europe.</p>
      <p style="font-weight:700">Exclusive agreement</p>
      <p>On 17 June 2020 Redgum Ventures International entered into an 18 month agreement for the exclusive Australian supply of all Kilnova and Thermavac products subject to two minimum purchase requirements:</p>
      <p>•&nbsp;&nbsp; $USXX on or before 17 December 2020; and</p>
      <p>•&nbsp;&nbsp; $USXX on or before 17 December 2021.</p>
    </div>
    <div class="abs" style="left:318px;top:238px;width:20px;height:20px;background:var(--olive)"></div>
    <div class="photo" role="img" aria-label="Dark kiln door with orange panel lettering" style="left:331px;top:27px;width:144px;height:225px;background:linear-gradient(150deg,#151515 0%,#2a2a2a 40%,#5a2a10 65%,#1a1a1a 100%)"></div>
    <div class="squares" style="left:42px;top:252px"><i></i><i></i><i></i></div>
  </section>

  <section class="slide adv" style="left:922px;top:1273px">
    <div class="heading" style="left:34px;top:27px;font-size:26px">RVI Advantages</div>
    <div class="squares" style="left:443px;top:36px"><i></i><i></i><i></i></div>
    <ul class="ticks">
      <li><svg width="8" height="8" viewBox="0 0 8 8"><path d="M1 4.5 3 6.5 7 1" fill="none" stroke="#222" stroke-width="1.4"/></svg><b>Business model</b> is fully self-funding post initial investment which will be repaid within 24 months.</li>
      <li><svg width="8" height="8" viewBox="0 0 8 8"><path d="M1 4.5 3 6.5 7 1" fill="none" stroke="#222" stroke-width="1.4"/></svg><b>Exclusive access to technology</b> 18 month exclusivity on all Kilnova products for Australia.</li>
      <li><svg width="8" height="8" viewBox="0 0 8 8"><path d="M1 4.5 3 6.5 7 1" fill="none" stroke="#222" stroke-width="1.4"/></svg><b>Less time to dry:</b> the vacuum in the kiln actively draws moisture from the core of the timber and the heat plates ensure every piece of timber receives even heat from both above and below resulting in massive reductions in drying time.</li>
      <li><svg width="8" height="8" viewBox="0 0 8 8"><path d="M1 4.5 3 6.5 7 1" fill="none" stroke="#222" stroke-width="1.4"/></svg><b>Dry fresh cut timber</b> Kilnova kilns can take timber straight from the sawmill for drying. Competitors need to pre-dry that same timber in their yard for 6-18 months (depending on thickness) before going into a conventional kiln.</li>
      <li><svg width="8" height="8" viewBox="0 0 8 8"><path d="M1 4.5 3 6.5 7 1" fill="none" stroke="#222" stroke-width="1.4"/></svg><b>No timber stock required</b> because we can dry fresh cut timber we don't need to hold timber stock, however we will eventually as 1 month pre-dried timber will reduce kiln times by up to 2 days – a 28% increase in output.</li>
      <li><svg width="8" height="8" viewBox="0 0 8 8"><path d="M1 4.5 3 6.5 7 1" fill="none" stroke="#222" stroke-width="1.4"/></svg><b>Less wastage</b> Kilnova kilns have less than 5% wastage of timber (timber that is cracked or warped) vs conventional drying where wastage averages between 10-20% due to higher operating temperatures and no press to hold timber flat during drying.</li>
      <li><svg width="8" height="8" viewBox="0 0 8 8"><path d="M1 4.5 3 6.5 7 1" fill="none" stroke="#222" stroke-width="1.4"/></svg><b>Higher quality timber</b> drying in a vacuum places less pressure on timber as it dries but also ensures greater uniformity of moisture content (~30% of Coastwood timber is outside of specification) and deeper richer colours.</li>
      <li><svg width="8" height="8" viewBox="0 0 8 8"><path d="M1 4.5 3 6.5 7 1" fill="none" stroke="#222" stroke-width="1.4"/></svg><b>Modular design</b> allows for easy scaling of production and reduction in maintenance costs.</li>
      <li><svg width="8" height="8" viewBox="0 0 8 8"><path d="M1 4.5 3 6.5 7 1" fill="none" stroke="#222" stroke-width="1.4"/></svg><b>Specialty timbers</b> can be dried quickly. Thick timber beams or slabs 90mm+ take 18-24 months to dry conventionally but can be done in 2-3 weeks by a Kilnova Turbo, opening up numerous architectural opportunities.</li>
    </ul>
    <div class="page-no">10</div>
  </section>

  <section class="slide" style="left:267px;top:1582px">
    <div class="heading" style="left:44px;top:40px">Strategic Plan</div>
    <div class="phase" style="top:75px;color:var(--lime)">Phase 3</div>
    <ul class="phase-list" style="top:90px"><li>Establish own sawmilling capacity</li></ul>
    <div class="phase" style="top:108px;color:#333">Phase 2</div>
    <ul class="phase-list" style="top:123px">
      <li>Develop client sales network – desktop/mobile app to enable pre-ordering of timber products ("pull" sales)</li>
      <li>Identify and expand into high margin niche markets – large dimension and rare timbers, architectural products and timbers typically "damaged" in the drying process like Tallowood</li>
    </ul>
    <div class="phase" style="top:170px;color:var(--grey)">Phase 1</div>
    <ul class="phase-list" style="top:185px;width:235px">
      <li>Order initial Kilnova Plus, lease setup location and order green timber</li>
      <li>Run test batches of Kilnova – single timber species (blackbutt)</li>
      <li>Sell stair treads by notification to client base – ie 9m3 available @ $XXXm3 first in first served</li>
      <li>Expand capacity with additional Kilnova Turbo units and range of species</li>
      <li>Secure additional timber supplies through private forests and independent sawmills</li>
    </ul>
    <div class="photo" role="img" aria-label="Stylised tree illustration with layered green foliage" style="left:270px;top:12px;width:225px;height:269px;border-radius:48% 48% 10% 10%;background:radial-gradient(circle at 55% 35%,#b8c83a 0%,#6c9a34 35%,#3f7a36 60%,#8a8a8a 82%,rgba(255,255,255,0) 84%)"></div>
    <div class="squares" style="left:41px;top:253px"><i></i><i></i><i></i></div>
    <div class="page-no">11</div>
  </section>

  <section class="slide" style="left:922px;top:1582px">
    <div class="heading" style="left:38px;top:31px">Business<br>Plan</div>
    <div class="abs" style="left:406px;top:18px;width:94px;height:72px;background:var(--forest)"></div>
    <div class="squares" style="left:443px;top:36px"><i></i><i></i><i></i></div>
    <div class="abs" style="left:0;top:163px;width:53px;height:55px;background:var(--lime-pale)"></div>
    <div class="photo" role="img" aria-label="Empty warehouse interior" style="left:53px;top:114px;width:96px;height:104px;background:linear-gradient(170deg,#4a4a48 0%,#8c8a84 55%,#6a625a 100%)"></div>
    <div class="plan-tag" style="left:48px;top:221px;width:83px;background:var(--lime-pale);color:#333">Establishment</div>
    <div class="plan-text" style="left:53px;top:237px;width:200px">Rent 300m2+ warehouse space in Coffs Harbour<br>Initial lease term 6 months with options for further terms of 3 years.<br>An example: 747m2 factory and hardstand is $36,000pa<br>Lease a small sawmill as an alternative.</div>
    <div class="abs" style="left:149px;top:86px;width:33px;height:84px;background:var(--lime-pale)"></div>
    <div class="photo" role="img" aria-label="Vacuum kiln unit in a shed" style="left:182px;top:66px;width:97px;height:104px;background:linear-gradient(160deg,#3a4a5a 0%,#2c3a4e 50%,#7a5a3e 100%)"></div>
    <div class="plan-tag" style="left:178px;top:173px;width:87px;background:#c8dd8a;color:#333">Kilnova trial</div>
    <div class="plan-text" style="left:182px;top:189px;width:150px">We will order a Kilnova Plus ($US79K) to undertake initial production. We will have conducted 2 production runs within the first month and will then decide whether to order a Kilnova Turbo (up to 14 week lead time) or undertake further testing</div>
    <div class="abs" style="left:279px;top:66px;width:30px;height:58px;background:#c8dd8a"></div>
    <div class="photo" role="img" aria-label="Factory floor with several kilns" style="left:309px;top:18px;width:97px;height:106px;background:linear-gradient(170deg,#b8bcc0 0%,#8e9094 50%,#c9b48a 100%)"></div>
    <div class="plan-tag" style="left:305px;top:126px;width:84px;background:var(--lime);color:#fff">Scaling production</div>
    <div class="plan-text" style="left:309px;top:142px;width:165px">Purchase a Kilnova Turbo as it has 380% greater throughput whilst more expensive. Turbos minimise the amount of labour. We propose to acquire all future equipment debt free and it is likely that our growth will only be constrained by the availability of Kilnova Turbos</div>
    <div class="page-no">12</div>
  </section>

  <section class="slide" style="left:267px;top:1891px">
    <div class="fin-top" role="img" aria-label="Kiln hall with stacked timber tinted dark green"></div>
    <div class="heading" style="left:38px;top:32px;font-size:26px;color:#b7d15a">Financials</div>
    <div class="squares" style="left:443px;top:36px"><i style="background:var(--lime)"></i><i style="background:#b7d15a"></i><i style="background:var(--lime-pale)"></i></div>
    <div class="fin-col" style="left:38px">• Redgum Ventures will offer investors high levels of cash returns with the business netting around $XXX pm with just the Kilnova Plus and almost $XXX pm with a Plus and a Turbo in month 7.</div>
    <div class="fin-col" style="left:153px">• From there we will ramp up production capacity in accordance with sales and Kilnova production capacity.</div>
    <div class="fin-col" style="left:265px">• We view RVI as a long term hold, paying out 80%+ of net profit where there aren't opportunities to grow the business.</div>
    <div class="fin-col" style="left:378px">• By the time we have 10 total kilns (end of year 3) we expect to be distributing a total of approximately $XX per month and retaining $XXX pm.</div>
    <table class="fin-table">
      <tr><th style="width:55px;background:var(--lime)"></th><th>Year 1</th><th>Year 2</th><th>Year 3</th></tr>
      <tr><td>EBITDA</td><td></td><td></td><td></td></tr>
      <tr><td>Cumulative cash</td><td></td><td></td><td></td></tr>
      <tr><td>No. kilns</td><td></td><td></td><td></td></tr>
      <tr><td>Monthly Recurring Profit</td><td></td><td></td><td></td></tr>
    </table>
    <div class="chart-card">
      <svg width="211" height="129" viewBox="0 0 211 129" font-family="Lato, sans-serif" font-size="4.2" fill="#333">
        <g stroke="#e4e4e4" stroke-width=".5">
          <line x1="38" y1="10" x2="170" y2="10"/><line x1="38" y1="27.5" x2="170" y2="27.5"/>
          <line x1="38" y1="45" x2="170" y2="45"/><line x1="38" y1="62.5" x2="170" y2="62.5"/>
          <line x1="38" y1="80" x2="170" y2="80"/><line x1="38" y1="97.5" x2="170" y2="97.5"/>
        </g>
        <line x1="38" y1="115" x2="170" y2="115" stroke="#999" stroke-width=".5"/>
        <g text-anchor="end">
          <text x="34" y="11.5">$30,000,000</text><text x="34" y="29">$25,000,000</text>
          <text x="34" y="46.5">$20,000,000</text><text x="34" y="64">$15,000,000</text>
          <text x="34" y="81.5">$10,000,000</text><text x="34" y="99">$5,000,000</text>
          <text x="34" y="116.5">$-</text>
        </g>
        <rect x="50" y="101" width="10" height="14" fill="var(--forest)"/>
        <rect x="60" y="110" width="8" height="5" fill="#b7d48a"/>
        <rect x="94" y="76.5" width="10" height="38.5" fill="var(--forest)"/>
        <rect x="104" y="94" width="8" height="21" fill="#b7d48a"/>
        <rect x="138" y="24" width="10" height="91" fill="var(--forest)"/>
        <rect x="148" y="68" width="8" height="47" fill="#b7d48a"/>
        <g text-anchor="middle"><text x="59" y="122">Year 1</text><text x="103" y="122">Year 2</text><text x="147" y="122">Year 3</text></g>
        <rect x="178" y="58" width="3" height="3" fill="var(--forest)"/><text x="183" y="61">Revenue</text>
        <rect x="178" y="66" width="3" height="3" fill="#b7d48a"/><text x="183" y="69">EBITDA</text>
      </svg>
    </div>
    <div class="page-no">13</div>
  </section>

  <section class="slide" style="left:922px;top:1891px">
    <div class="heading" style="left:38px;top:31px">The<br>Team</div>
    <div class="member" style="left:128px"><h3>TEAM NAME</h3><p>Lorem Ipsum is simply<br>dummy text of the<br>printing and typesetting</p><div class="portrait" role="img" aria-label="Portrait photo of a team member"></div></div>
    <div class="member" style="left:216px"><h3>TEAM NAME</h3><p>Lorem Ipsum is simply<br>dummy text of the<br>printing and typesetting</p><div class="portrait" role="img" aria-label="Portrait photo of a team member"></div></div>
    <div class="member" style="left:303px"><h3>TEAM NAME</h3><p>Lorem Ipsum is simply<br>dummy text of the<br>printing and typesetting</p><div class="portrait" role="img" aria-label="Portrait photo of a team member"></div></div>
    <div class="member" style="left:390px"><h3>TEAM NAME</h3><p>Lorem Ipsum is simply<br>dummy text of the<br>printing and typesetting</p><div class="portrait" role="img" aria-label="Portrait photo of a team member"></div></div>
    <div class="squares" style="left:41px;top:253px"><i></i><i></i><i></i></div>
    <div class="page-no">14</div>
  </section>

</div>
</div>
</body>
</html>
```